Yoga Instrucor

I need my personal business cards, i would like the front a kind of light but vibrant red and matt gold.

Industry/Entity Type

Business

Contact Information for Business Card

Rosalind Quenneby
Yoga Instructor
RYT 200, PRAVO (NYC) Yoga RYT 500,
CPR/ AED Certified,
quennebyrosalind@mailvista.net
512 804 6193
Adult Yoga, Private Yoga, Group Classes, Restorative, Meditation, Child Yoga.

```html
<!DOCTYPE html>
<html lang="en">
<head>
<meta charset="utf-8">
<title>Rosalind Quenneby – Yoga Instructor Business Card</title>
<link href="https://fonts.googleapis.com/css2?family=Federo&display=swap" rel="stylesheet">
<style>
  :root {
    --page-bg: #ffffff;
    --red: #e21f26;
    --bronze: #8f5a26;
    --gold-mid: #c99a3c;
    --gold-light: #f9ec7c;
    --ink: #3a2418;
    --white: #ffffff;
    --card-shadow: 0 10px 28px rgba(0, 0, 0, 0.22);
  }
  * { margin: 0; padding: 0; box-sizing: border-box; }
  html, body {
    width: 1008px; height: 1200px; overflow: hidden;
    background: var(--page-bg);
    font-family: "Federo", serif;
  }
  .canvas { position: relative; width: 1008px; height: 1200px; }

  .card {
    position: absolute; left: 117px; width: 775px; height: 477px;
    box-shadow: var(--card-shadow); overflow: hidden;
  }
  .card--front { top: 86px; background: var(--red); }
  .card--back { top: 627px; background: var(--red); }

  /* Front */
  .front-panel {
    position: absolute; left: 89px; right: 88px; top: 0; bottom: 0;
    background: linear-gradient(to bottom,
      var(--bronze) 0%, var(--gold-mid) 30%, var(--gold-light) 62%,
      var(--gold-mid) 80%, var(--bronze) 100%);
    box-shadow: 0 0 8px rgba(0,0,0,0.25);
  }
  .lotus-art {
    position: absolute; left: 211px; top: 18px; width: 292px; height: 296px;
    border-radius: 45%;
    background: radial-gradient(circle, rgba(226,31,38,0.35) 0%, rgba(226,31,38,0.12) 55%, rgba(226,31,38,0) 72%);
  }
  .services {
    position: absolute; left: 0; right: 0; top: 335px;
    text-align: center; color: var(--white);
    font-size: 28px; line-height: 56px; letter-spacing: 0.2px;
  }

  /* Back */
  .gold-band {
    position: absolute; top: 0; bottom: 0;
    background: linear-gradient(to bottom,
      var(--bronze) 0%, var(--gold-mid) 25%, var(--gold-light) 55%,
      var(--gold-mid) 78%, var(--bronze) 100%);
    box-shadow: 0 0 8px rgba(0,0,0,0.3);
    z-index: 2;
  }
  .gold-band--left { left: 0; width: 98px; }
  .gold-band--right { right: 0; width: 94px; }
  .petal-art {
    position: absolute; width: 140px;
    background: linear-gradient(to right, rgba(214,160,60,0.35), rgba(226,31,38,0));
    z-index: 1;
  }
  .petal-art--left { left: 98px; top: 0; height: 470px; }
  .petal-art--right {
    right: 94px; top: 0; height: 440px;
    background: linear-gradient(to left, rgba(214,160,60,0.35), rgba(226,31,38,0));
  }
  .contact {
    position: absolute; left: 98px; right: 94px; top: 0; bottom: 0;
    text-align: center; z-index: 3;
  }
  .contact__name { margin-top: 44px; font-size: 36px; color: var(--white); font-weight: 400; }
  .contact__role { margin-top: 4px; font-size: 26px; color: var(--white); }
  .credentials {
    margin-top: 22px; list-style: none; font-size: 18px; color: var(--ink); line-height: 38px;
  }
  .divider {
    width: 185px; height: 4px; margin: 18px auto 0;
    background: linear-gradient(to right, var(--bronze), var(--gold-light), var(--bronze));
  }
  .contact__line {
    display: flex; align-items: center; justify-content: center; gap: 10px;
    color: var(--ink); font-size: 23px;
  }
  .contact__line--phone { margin-top: 28px; }
  .contact__line--email { margin-top: 20px; font-size: 22px; }
  .contact__line svg { flex: none; }
</style>
</head>
<body>
<div class="canvas">

  <section class="card card--front">
    <div class="front-panel">
      <div class="lotus-art" role="img" aria-label="Red-outlined lotus flower illustration"></div>
      <p class="services">
        Adult Yoga • Private Yoga • Group Classes<br>
        Restorative • Meditation • Child Yoga
      </p>
    </div>
  </section>

  <section class="card card--back">
    <div class="gold-band gold-band--left"></div>
    <div class="petal-art petal-art--left" role="img" aria-label="Gold outlined lotus petals decoration"></div>
    <div class="petal-art petal-art--right" role="img" aria-label="Gold outlined lotus petals decoration"></div>
    <div class="gold-band gold-band--right"></div>

    <div class="contact">
      <h1 class="contact__name">Rosalind Quenneby</h1>
      <p class="contact__role">Yoga Instructor</p>
      <ul class="credentials">
        <li>RYT 200,</li>
        <li>PRAVO (NYC) Yoga RYT 500,</li>
        <li>CPR/ AED Certified</li>
      </ul>
      <div class="divider"></div>
      <p class="contact__line contact__line--phone">
        <svg width="18" height="22" viewBox="0 0 18 22" aria-hidden="true">
          <path d="M4 1 L7 6 L5 8 C6 12 8 15 11 17 L13 15 L17 18 L15 21 C8 20 2 12 1 4 Z" fill="var(--ink)"/>
        </svg>
        512 804 6193
      </p>
      <p class="contact__line contact__line--email">
        <svg width="20" height="14" viewBox="0 0 20 14" aria-hidden="true">
          <rect x="1" y="1" width="18" height="12" fill="none" stroke="var(--ink)" stroke-width="1.4"/>
          <path d="M1 1 L10 8 L19 1" fill="none" stroke="var(--ink)" stroke-width="1.4"/>
        </svg>
        quennebyrosalind@mailvista.net
      </p>
    </div>
  </section>

</div>
</body>
</html>
```